Construction Company Website Design

I need a Website Design for a Construction Company. I have attached logo and business card design files (a.i) to match styles and text for the website. I will need design for 3 pages:
1. A Home page
2. A secondary page (will be different information pages)
3. A contact page with submision form
Website to look professional and match the 'theme' across all pages, using main colours / reverse colours as per design files. Must be clear it is a construction related website without being over the top. Happy for the construction related details (whether that be images/outlines/backgrounds etc to be fairly subtle and not overbearing on the contect of the pages. It will be the content that will be most important, not the images within.

Content has not yet been fully completed but attached is a site map. Each page will need a space for the insertion of the relevant heading and associated content for that particular page. Example can be used as per attached map. If it is preferable to have content completed for this to be a more succesful project please advise and I will complete and submit.

Target Market(s)

Clients for potential construction projects. These could be a range of people. All would be very professional, well educated and put a substantial expection on the quality of website provided.

Industry/Entity Type

Construction

Number of Pages Required

3 page

Font styles to use
Serif
Sans Serif
Other font styles liked:
• fonts preferable as per design files provided unless designer beleives a different font would suit better

Requirements
Must have
• Colour scheme to match logo and business card files provided. Fonts that match as per provided files. Pages must be consistent with the theme carrying across all pages. All pages must have contact details at the bottom of the page.
• Contents of page 1 - 'Home page': multiple tab options / logo link
• Contents of page 2 - 'Secondary page': Top and side navigation / area for information and/or images.
• Contents of page - 'Contact us page': Top and side navigation / Submission form / area for logos such as linkdin, facebook etc.
Nice to have
• Would be good to have a or some generic construction related images - outlines / shadows / effects etc. These might be background images or outlines related to the relevant industry and are consistent across the pages. Could be outlines of buildings, images of men with hardhats etc etc. Good to see colour scheme as per design files used
Should not have
• No pictures of houses. Generally no photos. If any imagery of people must not show faces/details.

```html
<!DOCTYPE html>
<html lang="en">
<head>
<meta charset="utf-8">
<title>Halvard Build</title>
<link rel="stylesheet" href="https://fonts.googleapis.com/css2?family=Montserrat:wght@400;500;600;700&display=swap">
<style>
:root{
  --blue:#00aaec;
  --blue-light:#b7e6fa;
  --ink:#3c3c3c;
  --muted:#8a8a8a;
  --field:#ececec;
  --dark-btn:#555555;
  --footer:#1e1e1e;
  --white:#ffffff;
}
*{margin:0;padding:0;box-sizing:border-box}
html,body{width:686px;height:1200px;overflow:hidden;background:var(--white)}
body{font-family:'Montserrat',sans-serif;color:var(--ink);position:relative}
.abs{position:absolute}
.center{text-align:center}

/* header */
.site-header{position:absolute;left:0;top:0;width:686px;height:43px;background:var(--white)}
.brand{position:absolute;left:92px;top:13px;font-size:13px;font-weight:600;color:var(--ink);letter-spacing:1.5px;display:flex;align-items:center;gap:6px}
.brand-dot{width:8px;height:8px;background:var(--blue)}
.main-nav a{position:absolute;top:17px;font-size:6.5px;color:var(--ink);text-decoration:none;font-weight:500}
.main-nav a.active{color:var(--blue)}
.nav-cta{position:absolute;left:552px;top:15px;width:42px;height:14px;background:var(--blue);border-radius:2px}

/* hero */
.hero{position:absolute;left:0;top:43px;width:686px;height:281px;background:var(--blue);overflow:hidden}
.hero-art{position:absolute;left:240px;top:25px;width:220px;height:235px;background:radial-gradient(ellipse at center,rgba(255,255,255,.22),rgba(255,255,255,0) 70%)}
.hero h1{position:absolute;left:0;top:88px;width:686px;text-align:center;color:var(--white);font-size:16.5px;font-weight:600;line-height:20px}
.hero p{position:absolute;left:0;top:137px;width:686px;text-align:center;color:var(--white);font-size:8.5px;font-weight:500}
.hero-btn{position:absolute;left:305px;top:165px;width:75px;height:21px;border-radius:11px;background:var(--dark-btn);color:var(--white);font-size:6.5px;font-weight:600;display:flex;align-items:center;justify-content:center}
.slide-arrow{position:absolute;top:130px;width:22px;height:22px;border-radius:50%;background:var(--white);display:flex;align-items:center;justify-content:center}
.scroll-hint{position:absolute;left:319px;top:252px;width:48px;text-align:center;color:var(--white);font-size:6px;font-weight:600}
.scroll-hint span{display:block;border-bottom:1px solid var(--white);padding-bottom:2px;margin-bottom:1px}

/* services */
.section-title{position:absolute;left:0;width:686px;text-align:center;font-size:14px;font-weight:700;color:var(--ink)}
.service{position:absolute;top:410px;width:137px;height:141px;text-align:center}
.service.featured{border:1px solid #dcebf7;background:#f7fbfe;border-radius:3px;box-shadow:0 1px 4px rgba(0,120,200,.08)}
.service svg{position:absolute;left:56px;top:34px}
.service h3{position:absolute;left:0;top:84px;width:100%;font-size:7px;font-weight:600;color:var(--blue)}
.service p{position:absolute;left:8px;top:100px;width:121px;font-size:6px;line-height:9.5px;color:var(--muted)}
.btn-small{position:absolute;background:var(--blue);color:var(--white);font-size:5.5px;font-weight:700;display:flex;align-items:center;justify-content:center;border-radius:2px;box-shadow:0 1px 2px rgba(0,0,0,.2)}

/* about band */
.band{position:absolute;left:0;top:635px;width:686px;height:270px}
.band h2{position:absolute;top:707px;font-size:13.5px;font-weight:700;color:var(--white)}
.about-text{position:absolute;left:92px;top:734px;width:210px;font-size:6.6px;line-height:10.3px;font-weight:700;color:var(--white)}
.about-text p+p{margin-top:10px}
.project-frame{position:absolute;left:360px;top:732px;width:233px;height:120px;border-radius:3px;background:linear-gradient(135deg,#f4f4f4,#dcdcdc);box-shadow:0 1px 4px rgba(0,0,0,.15)}
.dots{position:absolute;left:441px;top:864px;display:flex;gap:4.4px}
.dots i{width:5px;height:5px;border-radius:50%;border:1px solid var(--white)}
.dots i.on{background:var(--white)}

/* contact */
.contact-item{position:absolute;left:110px;width:120px;text-align:center;font-size:6.2px;line-height:11px;color:var(--ink)}
.contact-item svg{display:block;margin:0 auto 2px}
.field{position:absolute;background:var(--field);font-size:6px;color:var(--muted);padding:7px 9px}

/* footer */
.site-footer{position:absolute;left:0;top:1171px;width:686px;height:29px;background:var(--footer)}
.footer-brand{position:absolute;left:92px;top:8px;font-size:12px;font-weight:600;color:#6a6a6a;letter-spacing:1.5px}
.copyright{position:absolute;right:92px;top:11px;font-size:5.8px;color:#9a9a9a}
.copyright span{color:var(--blue)}
</style>
</head>
<body>

<header class="site-header">
  <div class="brand"><span>HALVARD BUILD</span><span class="brand-dot"></span></div>
  <nav class="main-nav">
    <a class="active" style="left:333px">About Us</a>
    <a style="left:394px">Services</a>
    <a style="left:440px">Projects</a>
    <a style="left:485px">Culture</a>
    <a style="left:525px">News</a>
  </nav>
  <div class="nav-cta"></div>
</header>

<section class="hero">
  <div class="hero-art" role="img" aria-label="Faint hand-sketched outline of a building"></div>
  <h1>Welcome To The Halvard Build<br>Your Perfect Construction</h1>
  <p>Lorem ipsum dolor sit amet, consectetur adipiscing elit, sed do eiusmod tempo</p>
  <div class="hero-btn">Learn More</div>
  <div class="slide-arrow" style="left:55px"><svg width="8" height="8" viewBox="0 0 8 8"><path d="M5 1 2 4l3 3" fill="none" stroke="#333" stroke-width="1.2"/></svg></div>
  <div class="slide-arrow" style="left:608px"><svg width="8" height="8" viewBox="0 0 8 8"><path d="M3 1l3 3-3 3" fill="none" stroke="#333" stroke-width="1.2"/></svg></div>
  <div class="scroll-hint"><span>Click Here</span><svg width="8" height="5" viewBox="0 0 8 5"><path d="M1 1l3 3 3-3" fill="none" stroke="#fff" stroke-width="1.2"/></svg></div>
</section>

<h2 class="section-title" style="top:371px">HALVARD BUILD SERVICES</h2>

<div class="service" style="left:109px">
  <svg width="26" height="22" viewBox="0 0 26 22"><g fill="#444"><rect x="2" y="8" width="8" height="14"/><rect x="10" y="2" width="8" height="20"/><rect x="18" y="11" width="6" height="11"/></g><g fill="#fff"><rect x="4" y="11" width="2" height="2"/><rect x="4" y="15" width="2" height="2"/><rect x="12" y="5" width="2" height="2"/><rect x="12" y="9" width="2" height="2"/><rect x="12" y="13" width="2" height="2"/><rect x="20" y="14" width="2" height="2"/></g></svg>
  <h3>Commercial</h3>
  <p>Lorem ipsum dolor sit amet, consectetur adipiscing elit, sed do eiusmod tempor incididunt ut</p>
</div>
<div class="service featured" style="left:273px">
  <svg width="26" height="22" viewBox="0 0 26 22"><path d="M13 1 2 9h3v12h16V9h3z" fill="none" stroke="#444" stroke-width="1.6"/><g fill="#444"><rect x="8" y="11" width="3" height="3"/><rect x="15" y="11" width="3" height="3"/><rect x="11" y="15" width="4" height="6"/></g></svg>
  <h3>Residential</h3>
  <p>Lorem ipsum dolor sit amet, consectetur adipiscing elit, sed do eiusmod tempor incididunt ut</p>
</div>
<div class="service" style="left:440px">
  <svg width="26" height="22" viewBox="0 0 26 22"><g stroke="#333" stroke-width="3" stroke-linecap="round"><path d="M6 20 19 6"/><path d="M7 6l13 14"/></g><path d="M3 2h8l2 4-3 2z" fill="#333"/><circle cx="21" cy="4" r="3" fill="none" stroke="#333" stroke-width="2"/></svg>
  <h3>Building Maintainance</h3>
  <p>Lorem ipsum dolor sit amet, consectetur adipiscing elit, sed do eiusmod tempor incididunt ut</p>
</div>
<div class="btn-small" style="left:322px;top:573px;width:40px;height:16px">MORE</div>

<svg class="band" viewBox="0 635 686 270" width="686" height="270" aria-hidden="true">
  <polygon fill="#c8ecfb" points="0,650 60,644 200,665 380,641 480,648 630,643 686,660 686,905 0,905"/>
  <polygon fill="#00aaec" points="0,672 54,644 166,672 286,641 390,670 578,668 686,646 686,893 560,900 400,894 240,893 0,884"/>
  <polygon fill="#c8ecfb" points="0,884 240,882 400,889 560,894 686,884 686,895 560,901 400,895 240,894 0,890"/>
</svg>

<h2 class="abs" style="left:92px;top:707px;font-size:13.5px;font-weight:700;color:#fff">ABOUT HALVARD BUILD</h2>
<h2 class="abs" style="left:359px;top:707px;font-size:13.5px;font-weight:700;color:#fff">HALVARD BUILD PROJECTS</h2>
<div class="about-text">
  <p>Lorem ipsum dolor sit amet, consectetur adipiscing elit, sed do eiusmod tempor incididunt ut labore et dolore magna aliqua. Ut enim ad minim veniam, quis nostrud exercitation ullamco laboris nisi ut aliquip ex ea commodo consequat.</p>
  <p>Duis aute irure dolor in reprehenderit in voluptate velit esse cillum dolore eu fugiat nulla pariatur. Excepteur sint occaecat cupidatat non proident, sunt in culpa qui officia deserunt mollit anim id est laborum.</p>
</div>
<div class="project-frame" role="img" aria-label="Line drawing of a modern multi-storey building project"></div>
<div class="dots"><i class="on"></i><i></i><i></i><i></i><i></i><i></i><i></i><i></i><i></i></div>

<h2 class="section-title" style="top:950px">CONTACT US</h2>

<div class="contact-item" style="top:1001px">
  <svg width="7" height="9" viewBox="0 0 7 9"><path d="M3.5 0A3.2 3.2 0 0 0 .3 3.2C.3 5.6 3.5 9 3.5 9s3.2-3.4 3.2-5.8A3.2 3.2 0 0 0 3.5 0z" fill="#00aaec"/><circle cx="3.5" cy="3.2" r="1.2" fill="#fff"/></svg>
  Lorem ipsum is dummy text<br>industry.
</div>
<div class="contact-item" style="top:1049px">
  <svg width="8" height="8" viewBox="0 0 8 8"><path d="M1.5.5 3 2.5 2 3.6a5 5 0 0 0 2.4 2.4L5.5 5l2 1.5-1 1.3C3.5 7.8.2 4.5.2 1.5z" fill="#00aaec"/></svg>
  +1 555 010 2030
</div>
<div class="contact-item" style="top:1085px">
  <svg width="9" height="7" viewBox="0 0 9 7"><rect width="9" height="7" fill="#00aaec"/><path d="M0 0l4.5 3.8L9 0" fill="none" stroke="#fff" stroke-width=".8"/></svg>
  hello@halvardbuild.com
</div>

<div class="field" style="left:289px;top:1000px;width:145px;height:21px">Name</div>
<div class="field" style="left:449px;top:1000px;width:144px;height:21px">Email</div>
<div class="field" style="left:289px;top:1035px;width:304px;height:64px">Message</div>
<div class="btn-small" style="left:289px;top:1112px;width:41px;height:17px">SUBMIT</div>

<footer class="site-footer">
  <div class="footer-brand">HALVARD BUILD</div>
  <div class="copyright">Copyrights©2018 <span>Halvard Build</span> . Allrights are reserved.</div>
</footer>

</body>
</html>
```